Calvera fine stockings - sexy cardboard box design needed!

We need a packaging design for a new online company based in Sydney called 'Calvera Hosiery'. We will be selling sexy stockings to our customers by Italian designers. We mainly feature lace stockings, an example of which, can be seen here:
http://www.brindelatessuti.example/italy-FASHION-WINTER

The design should be a cardboard pull out box, black in colour with the logo on the cover. We are looking for the logo to communicate sophistication and sexiness.

Examples of cardboard box shapes we would like are:
http://www.tradovex.example/product-gs/583016294/High_quality_drawer_paper_box.html

http://www.tradovex.example/product-gs/536192047/Cardboard_drawer_box.html

29 December:
I submitted a note when I extended the deadline, but cannot see it, so will write here for clarification. It has been difficult to choose the best design as the designs submitted were of such high quality. I want to have some people judge the designs, but because of the Christmas Season I have extended the deadline so that this can be done. Thanks.

Target Market(s)

The working professional woman.

Industry/Entity Type

Fashion

Requirements
Must have
• The words "Calvera Hosiery" on the cover of the box.

The box should be a sliding drawer.

The box size should be: (22*15*2.5cm).

Washing instructions and recycling logos on the back of the box. See example of uploaded file.

Nice to have
• It would be nice to have the background of the box a dark colour, maybe charcoal? But we are open to all ideas.
Should not have
• A stock photo on cover of box.

```html
<!DOCTYPE html>
<html lang="en">
<head>
<meta charset="utf-8">
<title>Calvera Hosiery – Box Cover</title>
<link href="https://fonts.googleapis.com/css2?family=Cormorant+Garamond:wght@500&display=swap" rel="stylesheet">
<style>
  :root {
    --page-bg: #ffffff;
    --cover-charcoal: #24272a;
    --lace-band: #3b3e41;
    --lace-band-light: #46494c;
    --ribbon-grey: #5b5e61;
    --name-white: #f2f2f2;
  }
  * { margin: 0; padding: 0; box-sizing: border-box; }
  html, body {
    width: 1200px;
    height: 900px;
    overflow: hidden;
    background: var(--page-bg);
  }
  .canvas {
    position: relative;
    width: 1200px;
    height: 900px;
  }
  .box-cover {
    position: absolute;
    left: 344px;
    top: 70px;
    width: 516px;
    height: 756px;
    background: var(--cover-charcoal);
    overflow: hidden;
  }
  .cover-art {
    position: absolute;
    inset: 0;
    width: 100%;
    height: 100%;
  }
  .brand-name {
    position: absolute;
    left: 170px;
    width: 316px;
    top: 572px;
    text-align: center;
    font-family: "Cormorant Garamond", "Garamond", serif;
    font-weight: 500;
    font-size: 46px;
    line-height: 1;
    letter-spacing: 0.5px;
    color: var(--name-white);
    white-space: nowrap;
  }
</style>
</head>
<body>
  <main class="canvas">
    <section class="box-cover">
      <svg class="cover-art" viewBox="0 0 516 756" xmlns="http://www.w3.org/2000/svg">
        <defs>
          <linearGradient id="laceTone" x1="0" y1="0" x2="1" y2="1">
            <stop offset="0" stop-color="var(--lace-band-light)"/>
            <stop offset="1" stop-color="var(--lace-band)"/>
          </linearGradient>
        </defs>
        <path class="lace-band" role="img" aria-label="Grey floral lace pattern running down the left edge of the cover"
              d="M0,0 L124,0 C136,130 126,260 96,390 C66,520 56,630 68,756 L0,756 Z"
              fill="url(#laceTone)"/>
        <path class="ribbon-curve"
              d="M136,0 L150,0 C158,150 138,290 114,400 C88,530 86,650 102,756 L88,756 C72,650 74,530 100,400 C124,290 144,150 136,0 Z"
              fill="var(--ribbon-grey)"/>
      </svg>
      <h1 class="brand-name">Calvera Hosiery</h1>
    </section>
  </main>
</body>
</html>
```